Business Card for Veltrano, a french tech company

Tech company
New technologies
Serious design
Dark theme

User info :
Name: Mathis CORLAVE
Position: Co-Founder & CEO
Tel: (+33) 6 58 24 90 37
Email: mathis@veltrano.io
Website: www.veltrano.io
Address: 17 rue des Tanneurs 69002 LYON

Attached is the business logo file.

```html
<!DOCTYPE html>
<html lang="fr">
<head>
<meta charset="utf-8">
<title>Veltrano – Carte de visite</title>
<link rel="stylesheet" href="https://fonts.googleapis.com/css2?family=Open+Sans:wght@400;600;800&display=swap">
<style>
  :root {
    --bg: #e4e4e6;
    --magenta: #e3139b;
    --violet: #8d4bb0;
    --navy: #1b1f4b;
    --ink: #3a3a44;
    --paper: #ffffff;
    --rule-start: #e3139b;
    --rule-end: #d9c6ea;
  }
  * { box-sizing: border-box; margin: 0; padding: 0; }
  html, body { width: 1200px; height: 800px; overflow: hidden; }
  body {
    background: var(--bg);
    font-family: "Open Sans", sans-serif;
    display: flex;
    align-items: center;
    justify-content: center;
    gap: 60px;
  }
  .card {
    width: 520px;
    height: 300px;
    border-radius: 4px;
    position: relative;
    overflow: hidden;
    box-shadow: 0 10px 28px rgba(0,0,0,0.14);
  }
  .card--front {
    background: linear-gradient(150deg, var(--magenta) 0%, #c02ea3 50%, var(--violet) 100%);
  }
  .card--front .brand {
    position: absolute;
    left: 44px;
    top: 46px;
    color: var(--paper);
    font-weight: 800;
    font-size: 50px;
    letter-spacing: 3px;
    text-transform: uppercase;
    line-height: 1;
  }
  .card--back { background: var(--paper); }
  .card--back .brand {
    position: absolute;
    right: 36px;
    top: 40px;
    color: var(--navy);
    font-weight: 800;
    font-size: 40px;
    letter-spacing: 2px;
    text-transform: uppercase;
    line-height: 1;
  }
  .contact {
    position: absolute;
    left: 36px;
    top: 112px;
    width: 250px;
    color: var(--ink);
    font-size: 13px;
    line-height: 1.35;
  }
  .contact__name { color: var(--magenta); font-weight: 600; font-size: 14px; }
  .contact__name span { color: var(--violet); }
  .contact__role { margin-bottom: 10px; }
  .contact__list { list-style: none; }
  .contact__item { display: flex; align-items: center; gap: 7px; margin-bottom: 2px; }
  .contact__item svg { width: 12px; height: 12px; flex: none; fill: var(--navy); }
  .contact__rule {
    height: 1px;
    margin: 6px 0 6px;
    background: linear-gradient(90deg, var(--rule-start), var(--rule-end));
  }
</style>
</head>
<body>
  <section class="card card--front" aria-label="Recto">
    <div class="brand">Veltrano</div>
  </section>

  <section class="card card--back" aria-label="Verso">
    <div class="brand">Veltrano</div>
    <div class="contact">
      <p class="contact__name">Mathis <span>CORLAVE</span></p>
      <p class="contact__role">Co-Founder &amp; CEO</p>
      <ul class="contact__list">
        <li class="contact__item">
          <svg viewBox="0 0 24 24" aria-hidden="true"><path d="M6.6 10.8a15.2 15.2 0 0 0 6.6 6.6l2.2-2.2a1 1 0 0 1 1-.25 11.4 11.4 0 0 0 3.6.57 1 1 0 0 1 1 1V20a1 1 0 0 1-1 1A17 17 0 0 1 3 4a1 1 0 0 1 1-1h3.5a1 1 0 0 1 1 1c0 1.25.2 2.45.57 3.57a1 1 0 0 1-.25 1z"/></svg>
          (+33) 6 58 24 90 37
        </li>
        <li class="contact__item">
          <svg viewBox="0 0 24 24" aria-hidden="true"><path d="M2 5h20v14H2zm2 2v.5l8 5 8-5V7l-8 5z"/></svg>
          mathis@veltrano.io
        </li>
        <li class="contact__item">
          <svg viewBox="0 0 24 24" aria-hidden="true"><path d="M12 2a10 10 0 1 0 0 20 10 10 0 0 0 0-20zm6.9 6h-3a15.6 15.6 0 0 0-1.3-3.9A8 8 0 0 1 18.9 8zM12 4c.8 1.2 1.5 2.5 1.9 4h-3.8c.4-1.5 1.1-2.8 1.9-4zM4.3 14a8 8 0 0 1 0-4h3.4a16.5 16.5 0 0 0 0 4zm.8 2h3a15.6 15.6 0 0 0 1.3 3.9A8 8 0 0 1 5.1 16zm3-8h-3a8 8 0 0 1 4.3-3.9A15.6 15.6 0 0 0 8.1 8zM12 20c-.8-1.2-1.5-2.5-1.9-4h3.8c-.4 1.5-1.1 2.8-1.9 4zm2.3-6H9.7a14.7 14.7 0 0 1 0-4h4.6a14.7 14.7 0 0 1 0 4zm.3 5.9a15.6 15.6 0 0 0 1.3-3.9h3a8 8 0 0 1-4.3 3.9zm1.7-5.9a16.5 16.5 0 0 0 0-4h3.4a8 8 0 0 1 0 4z"/></svg>
          www.veltrano.io
        </li>
      </ul>
      <div class="contact__rule"></div>
      <p class="contact__address">17 rue des Tanneurs 69002 LYON</p>
    </div>
  </section>
</body>
</html>
```